Corvale Brochure - A new residential property investment development in Brisbane Queensland *

I need a brochure to entice and inspire customers of financial planners and alike to buy our investment property development, Corvale in Greenbank, Australia.

The brochure will be approximately 16 - 18 pages long and will follow a similar format (including maps etc) to the once attached in the uploaded files, however it is important that it has it's own unique style and brand identify. You will have access to all the renders, maps and autocad drawings that will need to be included in the brochure and will be linked in my dropbox link below.

The brochure should feel sophisticated and use the logo we've previously had developed on pixel forum. The background and text should also match the style guidelines of our logo's although happy for you to to get creative with the background as long as it is relevant and fits with the colours. For example stock photo's of tree's, people playing, sunlight etc are great - although the context should be in Australia.

There will be a bit of back and forth once I select the winning designer to ensure the brochure is perfect. I'll also need individual files of the masterplan.

Look forward to seeing your designs.

https://www.filemarrow.net/sh/qtmzx8v2pk4hd0r/BBKw7tnP3_QZmvUe9Lh4rxsk?dl=0

Target Market(s)

Financial Planners and their consumer customers

Industry/Entity Type

Real Estate Development

Font styles to use
Other font styles liked:
• Monserrat - as per branding guidelines

Requirements
Must have
• At least all the elements that exist in the example brochures and outlined in the content

dropbox link - https://www.filemarrow.net/sh/qtmzx8v2pk4hd0r/BBKw7tnP3_QZmvUe9Lh4rxsk?dl=0

```html
<!DOCTYPE html>
<html lang="en">
<head>
<meta charset="utf-8">
<title>Corvale Brochure – Amenities Spread</title>
<link href="https://fonts.googleapis.com/css2?family=Montserrat:wght@300;400;500;600&display=swap" rel="stylesheet">
<style>
  :root {
    --backdrop: #9c9c9c;
    --page-white: #f7f8f9;
    --night-blue-dark: #15263b;
    --night-blue-mid: #2a4563;
    --night-blue-light: #5c7d9f;
    --brand-blue: #2f6fa8;
    --ink: #4b5662;
    --heading-ink: #3a5f86;
    --on-photo: #e8eef5;
  }
  * { box-sizing: border-box; margin: 0; padding: 0; }
  html, body {
    width: 1200px; height: 900px; overflow: hidden;
    background: var(--backdrop);
    font-family: "Montserrat", sans-serif;
  }
  .spread {
    position: absolute; left: 40px; top: 250px;
    width: 1120px; height: 400px;
    display: flex;
    box-shadow: 0 14px 30px rgba(0,0,0,0.25);
  }
  .page { position: relative; width: 560px; height: 400px; }

  /* Left page – full-bleed photo */
  .page--photo { overflow: hidden; }
  .photo-fill {
    position: absolute; inset: 0;
    background:
      radial-gradient(ellipse 90px 220px at 88% 15%, rgba(200,215,235,0.55), transparent 70%),
      linear-gradient(180deg, var(--night-blue-dark) 0%, var(--night-blue-mid) 55%, var(--night-blue-light) 100%);
  }
  .photo-caption {
    position: absolute; left: 34px; top: 100px; width: 190px;
    color: var(--on-photo);
    font-weight: 300; font-size: 15px; line-height: 1.2;
  }

  /* Right page – amenities */
  .page--amenities { background: var(--page-white); padding: 30px 34px; }
  .amenities__title {
    font-weight: 500; font-size: 19px; color: var(--heading-ink);
    letter-spacing: 0.5px;
  }
  .amenities__intro {
    margin-top: 6px; font-size: 6.5px; line-height: 1.5; color: var(--ink);
  }
  .amenities__grid {
    position: absolute; left: 34px; right: 34px; top: 110px;
    display: grid; grid-template-columns: 1fr 1fr;
    column-gap: 50px; row-gap: 26px;
  }
  .amenity { text-align: center; }
  .amenity:nth-child(2) { margin-top: -22px; }
  .amenity:nth-child(4) { margin-top: -30px; }
  .amenity__icon { width: 24px; height: 24px; display: block; margin: 0 auto 6px; }
  .amenity__icon * { fill: none; stroke: var(--brand-blue); stroke-width: 1.4; stroke-linejoin: round; stroke-linecap: round; }
  .amenity__name {
    font-weight: 600; font-size: 7.5px; color: var(--brand-blue);
    line-height: 1.3; margin-bottom: 6px;
  }
  .amenity__text { font-size: 6px; line-height: 1.55; color: var(--ink); }
  .amenity__text + .amenity__text { margin-top: 5px; }
</style>
</head>
<body>
  <main class="spread">
    <section class="page page--photo">
      <div class="photo-fill" role="img" aria-label="Blue-toned photograph of a woman reading on a picnic rug in a tree-lined park at dusk"></div>
      <p class="photo-caption">A sense of privacy combined with easy access to amenities and services</p>
    </section>

    <section class="page page--amenities">
      <h1 class="amenities__title">Corvale</h1>
      <p class="amenities__intro">Corvale offers the best of both worlds with quiet suburban living and easy access to everyday amenities. The following places are all within a short drive, making life simple for families and professionals alike.</p>

      <div class="amenities__grid">
        <article class="amenity">
          <svg class="amenity__icon" viewBox="0 0 24 24" aria-hidden="true">
            <rect x="3" y="12" width="8" height="8"/>
            <rect x="12" y="12" width="8" height="8"/>
            <rect x="7" y="3" width="8" height="8" transform="rotate(12 11 7)"/>
          </svg>
          <h2 class="amenity__name">Child care centres, playing grounds and secondary schools</h2>
          <p class="amenity__text">Several child care centres and primary schools sit close by, with well known secondary schools and playing grounds only minutes away from the estate.</p>
        </article>

        <article class="amenity">
          <svg class="amenity__icon" viewBox="0 0 24 24" aria-hidden="true">
            <path d="M3 10h18v6H3z"/>
            <path d="M5 16v4M19 16v4M6 10V6h12v4"/>
          </svg>
          <h2 class="amenity__name">Local parks &amp; sporting facilities</h2>
          <p class="amenity__text">Open green spaces, walking tracks and sporting fields are spread across the area, giving residents plenty of room to relax and stay active.</p>
          <p class="amenity__text">A local shopping centre with a supermarket, cafes and everyday services is a short drive from home.</p>
        </article>

        <article class="amenity">
          <svg class="amenity__icon" viewBox="0 0 24 24" aria-hidden="true">
            <rect x="4" y="3" width="16" height="15" rx="2"/>
            <path d="M4 11h16M7 18v3M17 18v3"/>
            <circle cx="8" cy="14.5" r="1"/>
            <circle cx="16" cy="14.5" r="1"/>
          </svg>
          <h2 class="amenity__name">Transport</h2>
          <p class="amenity__text">Major arterial roads link the estate to the city and the coast, while nearby bus routes and train stations keep commuting quick and easy.</p>
        </article>

        <article class="amenity">
          <svg class="amenity__icon" viewBox="0 0 24 24" aria-hidden="true">
            <circle cx="12" cy="12" r="9"/>
            <path d="M12 8v8M8 12h8"/>
          </svg>
          <h2 class="amenity__name">Medical centres and specialist support services</h2>
          <p class="amenity__text">Medical centres, a private hospital and specialist support services are all within easy reach for peace of mind.</p>
        </article>
      </div>
    </section>
  </main>
</body>
</html>
```